Flyer-Design für Pultrusionstechnologie
Zielgruppe
Wir sind eine europäische Vereinigung von Herstellern mit Pultrusionstechnologie. Unser Ziel ist, die Pultrusionstechnik bekannter zu machen, für Kunststoffhersteller und Kunden.
Aufgabenstellung
Der Text im Flyer ist von uns vorgegeben. Das Format des Flyers soll klassisch sein, A4, zweimal gefaltet.

```html
<!DOCTYPE html>
<html lang="en">
<head>
<meta charset="utf-8">
<title>Pultrusion Flyer – Inside Spread</title>
<link href="https://fonts.googleapis.com/css2?family=Heebo:wght@300;400;500&display=swap" rel="stylesheet">
<style>
  :root {
    --page-bg: #d6d6d6;
    --panel-white: #f7f7f7;
    --brand-blue: #1e73c8;
    --deep-blue: #0a4fa5;
    --deep-blue-dark: #074494;
    --on-blue: #e9eef7;
  }
  * { box-sizing: border-box; margin: 0; padding: 0; }
  html, body {
    width: 1200px; height: 864px; overflow: hidden;
    background: var(--page-bg);
    font-family: "Heebo", Arial, sans-serif;
  }
  .spread {
    position: absolute; left: 90px; top: 42px;
    width: 1020px; height: 780px;
    display: flex;
    box-shadow: 0 6px 24px rgba(0,0,0,0.12);
  }
  .panel {
    position: relative; width: 340px; height: 100%;
    background: var(--panel-white);
    padding: 0 30px 0 38px;
  }
  .panel--blue {
    background: linear-gradient(160deg, var(--deep-blue) 0%, var(--deep-blue-dark) 100%);
    color: var(--on-blue);
    padding: 0 24px 0 22px;
  }
  .marker {
    position: absolute; top: 58px; width: 23px; height: 25px;
    background: var(--brand-blue);
  }
  .marker--left { left: 38px; }
  .marker--right { right: 42px; }
  .panel-title {
    font-weight: 400; font-size: 37px; line-height: 44px;
    letter-spacing: 1.5px; text-transform: uppercase;
    color: var(--brand-blue);
  }
  .panel--blue .panel-title { color: var(--on-blue); }
  .panel-title--top { position: absolute; top: 122px; left: inherit; }
  .panel:first-child .panel-title--top { left: 38px; }
  .panel--blue .panel-title--top { left: 22px; }
  .panel-title--bottom { position: absolute; top: 506px; left: 22px; }
  .body-copy {
    font-size: 11px; line-height: 15px; font-weight: 400;
    color: var(--brand-blue);
  }
  .body-copy--bottom { position: absolute; top: 636px; left: 38px; right: 30px; }
  .panel--right .body-copy--bottom { left: 22px; right: 44px; }
  .body-copy a { color: inherit; font-weight: 500; text-decoration: none; }
  .intro {
    position: absolute; top: 248px; left: 22px; right: 40px;
    font-size: 11px; line-height: 15px; font-weight: 300;
  }
  .advantages {
    position: absolute; top: 300px; left: 32px; right: 30px;
    list-style: none;
  }
  .advantages li {
    position: relative; padding-left: 11px; margin-bottom: 6px;
    font-size: 11px; line-height: 15px; font-weight: 300;
    letter-spacing: 0.5px; text-transform: uppercase;
  }
  .advantages li::before {
    content: "•"; position: absolute; left: 0; top: 0; font-size: 8px;
  }
</style>
</head>
<body>
  <main class="spread">
    <section class="panel panel--left">
      <span class="marker marker--left"></span>
      <h2 class="panel-title panel-title--top">What is<br>pultrusion?</h2>
      <p class="body-copy body-copy--bottom">Pultrusion is an automated process for the continuous production of FRP (Fiber Reinforced Plastics) profiles with a constant cross section. The process is very well established with nearly unlimited possibilities. In the process, the use of various materials/ semi-finished products is possible.</p>
    </section>

    <section class="panel panel--blue">
      <h2 class="panel-title panel-title--top">Advantages of<br>pultrusion?</h2>
      <p class="intro">FRP-Profiles are perfect materials for the construction of structural elements. There are several advantages (e.g.):</p>
      <ul class="advantages">
        <li>Nearly no limitations in shape or length</li>
        <li>High lightweight potential (low density)</li>
        <li>Very high tensile strength</li>
        <li>Profiles are easy to transport and to install</li>
        <li>Corrosion and weather resistant</li>
        <li>Excellent chemical and biological resistance</li>
        <li>Nearly maintenance free usage</li>
        <li>Low thermal and electrical conductivity (GFRP)</li>
        <li>Transparent to electromagnetic waves</li>
      </ul>
    </section>

    <section class="panel panel--right">
      <span class="marker marker--right"></span>
      <h2 class="panel-title panel-title--bottom">Additional<br>information</h2>
      <p class="body-copy body-copy--bottom">You want to know more about pultrusion, technical specifications or our members? Please visit our website <a href="#">www.fibreprofile-network.eu</a> Find news articles, background documents and the largest pultrusion network in Europe. We are looking forward to your visit!</p>
    </section>
  </main>
</body>
</html>
```